Web Application UI Design

Looking for a light weight UI re-design with complete html files and images for an existing project. As you can see from the uploaded files, the current design is clunky. We are looking to redesign the web application with state of the art light weight UI (Must include bootstrap and should be able to support angular)

Requirements
Must have
• Must have lightweight design preferably with material and bootstrap design
Nice to have
• The screen shots I uploaded show that the design is clunky. I am looking for some new designs

```html
<!DOCTYPE html>
<html lang="en">
<head>
<meta charset="utf-8">
<title>Vantaplat – Edit Ingestion</title>
<link href="https://fonts.googleapis.com/css2?family=Source+Sans+3:wght@400;600;700&display=swap" rel="stylesheet">
<style>
:root{
  --sidebar:#2030c9;
  --sidebar-active:#1a28b0;
  --sidebar-text:#ffffff;
  --page:#f4f5f9;
  --surface:#ffffff;
  --field:#f3f3f5;
  --text:#222430;
  --muted:#5b5e6c;
  --accent:#2233dd;
  --line:#e6e7ee;
}
*{box-sizing:border-box;margin:0;padding:0}
html,body{width:1200px;height:675px;overflow:hidden}
body{font-family:"Source Sans 3",sans-serif;background:var(--page);color:var(--text);position:relative}
.sidebar{position:absolute;left:0;top:0;width:187px;height:675px;background:var(--sidebar);color:var(--sidebar-text)}
.brand{position:absolute;left:50px;top:14px;font-size:13px;font-weight:600}
.nav-item{position:absolute;left:0;width:187px;height:28px;display:flex;align-items:center;font-size:13px}
.nav-item svg.icon{position:absolute;left:20px;width:15px;height:15px}
.nav-item .label{position:absolute;left:49px}
.nav-item svg.chev{position:absolute;right:36px;width:9px;height:9px}
.nav-group{position:absolute;left:0;top:229px;width:187px;height:100px;background:var(--sidebar-active)}
.nav-sub{position:absolute;left:49px;font-size:12px}
.topbar{position:absolute;left:187px;top:0;right:0;height:45px;background:var(--surface);box-shadow:0 1px 3px rgba(0,0,0,.05)}
.search{position:absolute;left:49px;top:7px;width:544px;height:29px;background:var(--field);border-radius:3px;display:flex;align-items:center;font-size:12px;color:var(--muted)}
.search svg{margin:0 9px 0 12px;width:13px;height:13px}
.user{position:absolute;right:48px;top:13px;font-size:14px;font-weight:600}
.avatar{position:absolute;right:12px;top:5px;width:33px;height:33px;border-radius:50%;background:radial-gradient(circle at 50% 40%,#7a5a48,#2c221e)}
h1{position:absolute;left:236px;top:66px;font-size:17px;font-weight:600}
h2{position:absolute;top:155px;font-size:16px;font-weight:600}
.card{position:absolute;background:var(--surface);border-radius:3px;box-shadow:0 1px 4px rgba(30,40,90,.07)}
.field{position:absolute;background:var(--field);border-radius:3px;font-size:11px;color:var(--muted);padding-left:12px;display:flex;align-items:center}
.field.select{background:var(--surface);border:1px solid var(--line)}
.field.textarea{align-items:flex-start;padding-top:11px}
.field svg.chev{position:absolute;right:11px;top:50%;margin-top:-4px;width:9px;height:9px}
.more{position:absolute;background:var(--field);border-radius:3px;display:flex;align-items:center;justify-content:center}
.btn{position:absolute;top:500px;height:30px;border-radius:4px;font-size:12px;font-weight:600;display:flex;align-items:center;justify-content:center}
.btn-primary{background:var(--accent);color:#fff}
.btn-outline{border:1.5px solid var(--accent);color:var(--accent);background:var(--surface)}
</style>
</head>
<body>
<aside class="sidebar">
  <div class="brand">Vantaplat</div>
  <div class="nav-group"></div>
  <div class="nav-item" style="top:122px">
    <svg class="icon" viewBox="0 0 16 16" fill="none" stroke="#fff" stroke-width="1.4"><circle cx="8" cy="8" r="2.5"/><circle cx="8" cy="8" r="6"/></svg>
    <span class="label">Services</span></div>
  <div class="nav-item" style="top:157px">
    <svg class="icon" viewBox="0 0 16 16" fill="none" stroke="#fff" stroke-width="1.4"><rect x="2" y="2" width="5" height="5"/><rect x="9" y="2" width="5" height="5"/><rect x="2" y="9" width="5" height="5"/><rect x="9" y="9" width="5" height="5"/></svg>
    <span class="label">Dashboard</span>
    <svg class="chev" viewBox="0 0 10 10" fill="none" stroke="#fff" stroke-width="1.4"><path d="M2 3.5l3 3 3-3"/></svg></div>
  <div class="nav-item" style="top:193px">
    <svg class="icon" viewBox="0 0 16 16" fill="none" stroke="#fff" stroke-width="1.4"><path d="M6.5 9.5l3-3M5 8l-2 2a2 2 0 003 3l2-2M11 8l2-2a2 2 0 00-3-3L8 5"/></svg>
    <span class="label">Connectors</span>
    <svg class="chev" viewBox="0 0 10 10" fill="none" stroke="#fff" stroke-width="1.4"><path d="M2 3.5l3 3 3-3"/></svg></div>
  <div class="nav-item" style="top:229px">
    <svg class="icon" viewBox="0 0 16 16" fill="none" stroke="#fff" stroke-width="1.4"><path d="M2 8h9M8 4l4 4-4 4"/><path d="M14 3v10"/></svg>
    <span class="label">Ingestion</span>
    <svg class="chev" viewBox="0 0 10 10" fill="none" stroke="#fff" stroke-width="1.4"><path d="M2 6.5l3-3 3 3"/></svg></div>
  <div class="nav-sub" style="top:269px">Overview</div>
  <div class="nav-sub" style="top:301px">Activity</div>
  <div class="nav-item" style="top:343px">
    <svg class="icon" viewBox="0 0 16 16" fill="none" stroke="#fff" stroke-width="1.4"><rect x="2" y="2" width="12" height="12" rx="1"/><path d="M2 6h12M6 6v8"/></svg>
    <span class="label">WorkBench</span>
    <svg class="chev" viewBox="0 0 10 10" fill="none" stroke="#fff" stroke-width="1.4"><path d="M2 3.5l3 3 3-3"/></svg></div>
  <div class="nav-item" style="top:379px">
    <svg class="icon" viewBox="0 0 16 16" fill="none" stroke="#fff" stroke-width="1.4"><circle cx="8" cy="5.5" r="3"/><path d="M2.5 14c.5-3 2.8-4.5 5.5-4.5s5 1.5 5.5 4.5"/></svg>
    <span class="label">Administration</span>
    <svg class="chev" viewBox="0 0 10 10" fill="none" stroke="#fff" stroke-width="1.4"><path d="M2 3.5l3 3 3-3"/></svg></div>
</aside>

<header class="topbar">
  <div class="search">
    <svg viewBox="0 0 14 14" fill="none" stroke="#6a6d7a" stroke-width="1.5"><circle cx="6" cy="6" r="4.5"/><path d="M9.5 9.5l3 3"/></svg>
    Search Anything</div>
  <div class="user">Daniel Hargrove</div>
  <div class="avatar" role="img" aria-label="User profile photo"></div>
</header>

<h1>Edit Ingestion</h1>
<div class="field select" style="left:236px;top:102px;width:266px;height:32px;color:var(--text)">Korvel Demo
  <svg class="chev" viewBox="0 0 10 10" fill="none" stroke="#2233dd" stroke-width="1.5"><path d="M2 3.5l3 3 3-3"/></svg></div>

<h2 style="left:236px">Source</h2>
<section class="card" style="left:236px;top:193px;width:452px;height:311px"></section>
<div class="field" style="left:247px;top:211px;width:428px;height:28px">RDBMS<svg class="chev" viewBox="0 0 10 10" fill="none" stroke="#2233dd" stroke-width="1.5"><path d="M2 3.5l3 3 3-3"/></svg></div>
<div class="field" style="left:247px;top:254px;width:428px;height:28px">RDBMS 2.90L<svg class="chev" viewBox="0 0 10 10" fill="none" stroke="#2233dd" stroke-width="1.5"><path d="M2 3.5l3 3 3-3"/></svg></div>
<div class="field" style="left:247px;top:298px;width:428px;height:32px">MODEL_SCHEMA</div>
<div class="field textarea" style="left:247px;top:343px;width:428px;height:80px">SELECT Top 10 * from MODEL_SCHEMA</div>

<h2 style="left:697px">Target</h2>
<section class="card" style="left:697px;top:193px;width:451px;height:346px"></section>
<div class="field" style="left:709px;top:211px;width:427px;height:28px">Dataloom<svg class="chev" viewBox="0 0 10 10" fill="none" stroke="#2233dd" stroke-width="1.5"><path d="M2 3.5l3 3 3-3"/></svg></div>
<div class="field" style="left:709px;top:254px;width:427px;height:28px">Select Cluster<svg class="chev" viewBox="0 0 10 10" fill="none" stroke="#2233dd" stroke-width="1.5"><path d="M2 3.5l3 3 3-3"/></svg></div>
<div class="field" style="left:709px;top:297px;width:427px;height:32px">DLFS<svg class="chev" viewBox="0 0 10 10" fill="none" stroke="#2233dd" stroke-width="1.5"><path d="M2 3.5l3 3 3-3"/></svg></div>
<div class="field" style="left:709px;top:343px;width:357px;height:32px">DLFS</div>
<div class="more" style="left:1077px;top:343px;width:59px;height:32px"><svg width="14" height="4" viewBox="0 0 14 4" fill="#2233dd"><circle cx="2" cy="2" r="1.3"/><circle cx="7" cy="2" r="1.3"/><circle cx="12" cy="2" r="1.3"/></svg></div>
<div class="field" style="left:709px;top:386px;width:427px;height:32px">Fields separated by /t</div>
<div class="field" style="left:709px;top:434px;width:427px;height:34px">Lines separated by /n</div>

<div class="btn btn-primary" style="left:809px;width:103px">Save</div>
<div class="btn btn-primary" style="left:921px;width:104px">Save and Run</div>
<div class="btn btn-outline" style="left:1034px;width:104px">Cancel</div>
</body>
</html>
```